Zelmor Africa - Website Design Brief

Web Design Brief

ZELMOR AFRICA
WEBSITE DESIGN BRIEF

INTRODUCTION
ABOUT ZELMOR
• ZELMOR is a premier consulting firm that specialises in aiding global corporations and emerging businesses to enter and scale within Africa's dynamic markets. Through swift, actionable insights and innovative strategies, ZELMOR empowers clients to capitalise on Africa's untapped potential, thereby catering specifically to forward-thinking entities poised for exponential growth.

TASK DESCRIPTION
• Develop a 5-page website for ZELMOR.
• The primary goal is to present a clear and concise picture of our consulting firm, its Africa-centric experience, and its offerings to multinational clients looking for a professional partner to penetrate African markets or reclaim lost market share.

WEBSITE FRAMEWORK
Page Architecture:
• Home
o A powerful landing page that instantly communicates who ZELMOR is and what solutions it provides. Incorporate impactful visuals and calls-to-action.
• About
o A compelling narrative that illustrates ZELMOR's unique approach to consulting, dedication to Africa, and experience assisting multinational firms.
• Services
o A showcase of ZELMOR's successful projects and client testimonials. This page should build trust and credibility, demonstrating ZELMOR's ability to deliver exceptional results.
• Team
o Introduce up to 8 key team members, with each profile featuring a professional photo, name, title, and a brief bio showcasing the individual's skills, experiences, and contributions to ZELMOR's mission.
• Contact
o Clear and easy ways for visitors to contact ZELMOR for more information or to initiate a partnership.
• Footer
o Links to ZELMOR's social media profiles on Pictova and Workfolk, along with a privacy policy.
o Social links
o Pictova: https://www.instagram.com/zelmorafrica/
o Workfolk: https://www.linkedin.com/company/zelmorafrica/
o Privacy Policy
o Insert placeholder "lorem ipsum" text.
o Text will be provided with the revision round or ZELMOR will update text on site handover.

DESIGN INSPIRATION
• The website's design should evoke professionalism and elegance, with simple and clean lines inspired by site pages like:
o https://quendaro.example/
o https://quendaro.example/services/
o One aspect we particularly appreciate is how visitors can easily navigate by scrolling down to find what they're looking for and see everything they need to in an intuitive way on the home page
o What we don’t like about this site is how they navigate from the home page to other random pages – we like about to take you to the about page, and so on.

Branding Guidelines:
• See logo on Pixel Bazaar: Design #: 58170926
• We like the idea of the logo being black or white and have uploaded these options as well.
• Monochrome themes, with spots or splash of colour to highlight something is a style we appreciate.

Website Objectives and Goals:
• Our website's primary goal is to create a strong online presence, acting as a hub for potential clients to discover our credibility, reliability, and our ability to deliver exceptional results. It's essential that our website portrays professionalism, instils trustworthiness, and showcases our sincere dedication to Africa.

Target audience:
• ZELMOR's audience consists of businesses in mobile money, gaming, FMCG, beverage, and alcohol sectors, primarily Business Development Managers or Operations Managers who are seeking insight into their respective marketplaces.

Company Overview:
• ZELMOR stands out from the crowd as a consulting firm with a difference. Our dynamic team is fully dedicated to one mission: brand development within Africa.
• Unlike other companies that focus solely on online connectivity, we recognize the tremendous value in embracing the vibrant street culture that makes Africa so unique. Community engagement, empowerment, and expansion are at the forefront of everything we do.
• we recognize that unlocking business growth starts with a deep understanding of consumer behavior. It is this understanding that bridges the gap between companies and the communities that drive the cash economy. Our purpose is to reconnect businesses with the vibrant pulse of these essential local markets, injecting fresh vitality into their brands and propelling them towards resounding success in Africa.

Development to include:
• Basic SEO Setup:
o The website should be optimized for search engines, incorporating keywords, meta tags, and alt tags for images.
• Google Analytics Setup.
o To track website traffic and user behaviour for ongoing optimization.
• Google Crawling Setup
o The website needs to be easily indexed by Google, allowing it to appear in search results, and updated information effectively crawled by Google SEO and AHREFS scores.

PAGE CONTENT:
Home Page
• Background
o Option #1
o 4K video on home page, running on loop
o Bold Statement Text over Video
o Option #2
o Still Image
o Animated text making bold statement (e.g. our motto)

• Sections
o Contrast colour blocks or a way of making it clear that the next topic is a new topic.
o 5 sections
1. Home Main - Video + bold statement text
2. About - A paragraph and visual about us (lorem ipsum) that has a click through to our About Page (ignore how quendaro.example navigate, we think this is too complicated for our needs)
3. Services – communicated in some simple and powerful ways (we leave this open to you) – but keeping in mind it needs to be concise and professional.
4. Other - Something about our process that makes us unique (lorem ipsum text) and a placeholder image/animation.
5. Contact – a call-to-action button that takes you to our contact, but showcases a mobile number and email address.
6. Footer – as described in the previous section – placeholder for Pictova and Workfolk only.

About Page
• Don’t reference quendaro.example for this page.
• Main Section
o Bold statements and images
• History Section
o A story about us and our past
• Final Section
o Some of our comments and final thoughts

Services Page
• How https://quendaro.example/services/ is laid out is great – we prefer a light theme.
• 6 - 8 x icons with headings and a brief description text box, and a read more drop down – all as placeholders to be edited later.
• For ease of direction for this page, look to the link shared above.

Team
• Add Placeholders for up to 8 team members (we only have 4 now):
o Image placeholder
o Name placeholder
o Title placeholder
o Short Bio (lorem ipsum)

Contact
• Clear and easy ways for visitors to contact ZELMOR for more information or to initiate a partnership.

• Insert placeholder "lorem ipsum" text, we will provide the text with our revision round.
o Ideally an easy form process that gives the user some options or dropdowns to complete before submission – up to 3 would be sufficient.
o Require their name and contact details.

NOTE: Images to follow:

Target Market(s)

ZELMOR's audience consists of businesses in mobile money, gaming, FMCG, beverage, and alcohol sectors, primarily Business Development Managers or Operations Managers who are seeking insight into their respective marketplaces.

Industry/Entity Type

ZELMOR is a premier consulting firm that specialises in aiding global corporations and emerging businesses to enter and scale within Africa's dynamic markets

Coding

Coded - Design and coding required

Number of Pages Required

5+ page

Font styles to use
Sans Serif
Other font styles liked:
• Poppins Font Family

Colors

Designer to choose colors to be used in the design.

Requirements
Must have
• The primary goal is to present a clear and concise picture of our consulting firm, and it's specialisation in Africa - smooth and crisp UI with animations or transitions that imply we know our way around tecchnology is always helpful - but a Clean and responsive UI is most important.
Nice to have
• Reactive and animated transitions through sections or pages - not overdone - adds a professional feel to the site
Should not have
• We don't want too many colours, and we don't want it too dark - we want a monochrome theme, with accents of colour when relevant

```html
<!DOCTYPE html>
<html lang="en">
<head>
<meta charset="utf-8">
<title>Zelmor Africa – Brand Development within Africa</title>
<link rel="stylesheet" href="https://fonts.googleapis.com/css2?family=Jost:wght@300;400;500;600&display=swap">
<style>
:root{
  --blue:#0169c1;
  --blue-soft:#1a78c9;
  --black:#000;
  --process:#333333;
  --contact:#1e1e1e;
  --white:#fff;
  --muted:#d6d6d6;
}
*{margin:0;padding:0;box-sizing:border-box}
html,body{width:1200px;height:2662px;overflow:hidden}
body{font-family:'Jost',sans-serif;color:var(--white);background:var(--black);position:relative}
.abs{position:absolute}
section,header,footer{position:absolute;left:0;width:1200px;overflow:hidden}

/* header */
.site-header{top:0;height:62px;border-bottom:1px solid rgba(255,255,255,.35);z-index:3}
.brand{position:absolute;display:flex;align-items:center;gap:8px;font-weight:500;letter-spacing:.5px}
.brand .mark{border:2px solid var(--white)}
.site-header .brand{left:75px;top:17px;font-size:24px}
.site-header .brand .mark{width:26px;height:26px}
.main-nav a{position:absolute;top:23px;font-size:11.5px;color:var(--white);text-decoration:none}
.header-phone{position:absolute;right:75px;top:23px;font-size:12px;font-weight:500;display:flex;gap:5px;align-items:center}

/* hero */
.hero{top:0;height:524px;background:radial-gradient(ellipse at 50% 45%,#4a4742 0%,#302e2b 55%,#1f1e1c 100%)}
.play{left:569px;top:154px;width:62px;height:62px;border:1.5px solid var(--white);border-radius:50%}
.hero h1{position:absolute;left:0;width:1200px;top:240px;text-align:center;font-weight:500;font-size:44px;line-height:47px;letter-spacing:.5px}
.scroll-line{left:599px;top:426px;width:1px;height:66px;background:var(--white)}

/* section labels */
.label{position:absolute;left:0;display:flex;align-items:center;gap:12px;font-size:11px;font-weight:600;letter-spacing:.3px}
.label::before{content:"";width:125px;height:1px;background:var(--white)}

.btn{position:absolute;display:flex;align-items:center;height:31px;font-size:10.5px;padding-left:12px;color:var(--white);text-decoration:none}
.btn::before{content:"";position:absolute;left:0;top:0;width:31px;height:31px;border:1px solid var(--white)}
.btn.boxed::before{width:100%}

/* about */
.about{top:524px;height:582px;background:var(--blue)}
.about .lead{position:absolute;left:406px;top:118px;width:365px;font-size:22px;line-height:30px;font-weight:400}
.about .body{position:absolute;left:406px;top:316px;width:355px;font-size:11px;line-height:22.5px}
.photo{position:absolute}
.about .market{left:0;top:263px;width:331px;height:319px;background:linear-gradient(180deg,#a8b8c6 0%,#c8b9a8 45%,#9b6e55 100%)}
.about .street{left:869px;top:75px;width:331px;height:350px;background:linear-gradient(160deg,#7a4a3a 0%,#7e8a6a 40%,#b3aaa3 70%,#5a4d48 100%)}
.ghost-square{border:18px solid rgba(255,255,255,.09)}
.about .ghost-square{left:613px;top:409px;width:180px;height:200px}

/* services */
.services{top:1106px;height:662px;background:var(--black)}
.service-icon{left:264px;top:162px;width:67px;height:68px;border:2px solid var(--blue)}
.service-rule{left:382px;top:124px;width:1px;height:275px;background:#666}
.service-list{position:absolute;left:406px;top:134px;list-style:none;font-size:22px;line-height:44px}
.service-list .active{color:var(--blue-soft)}
.service-marker{left:380px;top:182px;width:3px;height:24px;background:var(--blue)}
.services .body{position:absolute;left:406px;top:445px;width:340px;font-size:10.5px;line-height:22.5px;font-weight:500}
.services .dash{left:794px;top:106px;width:406px;height:438px;background:linear-gradient(150deg,#5d86b8 0%,#2d5b8f 45%,#6c87a3 75%,#3e4e66 100%)}

/* process */
.process{top:1768px;height:470px;background:var(--process)}
.step{position:absolute;top:136px;width:172px}
.step svg{display:block}
.step h3{margin-top:22px;width:150px;font-size:13.5px;font-weight:500;line-height:19px}
.step p{margin-top:12px;font-size:10.5px;line-height:19px;color:var(--muted)}
.wave{position:absolute;top:158px}

/* contact */
.contact{top:2238px;height:424px;background:var(--contact)}
.contact .brand{left:137px;top:176px;font-size:48px;gap:14px;font-weight:500}
.contact .brand .mark{width:50px;height:50px;border-width:4px}
.contact h2{position:absolute;left:406px;top:117px;font-size:29px;font-weight:400}
.contact .sub{position:absolute;left:406px;top:175px;width:345px;font-size:18px;line-height:27px;font-weight:300}
.contact-list{position:absolute;left:820px;top:122px;list-style:none;font-size:14.5px}
.contact-list li{display:flex;align-items:center;gap:12px;height:30px}
.contact-list a{color:var(--white)}
.contact-list a.current{color:var(--blue-soft)}
.contact-list svg{flex:none}
.contact .ghost-square{left:1030px;top:262px;width:160px;height:170px;border-color:rgba(255,255,255,.06)}
.footer-rule{left:137px;top:350px;width:925px;height:1px;background:#555}
.copyright{position:absolute;left:0;width:1200px;top:379px;text-align:center;font-size:10px;font-weight:500}
.copyright span{color:var(--blue-soft)}
</style>
</head>
<body>

<section class="hero">
  <div class="abs play"><svg width="62" height="62" viewBox="0 0 62 62"><path d="M25 22 L38 31 L25 40Z" fill="#fff"/></svg></div>
  <h1>Brand Development<br>within Africa.</h1>
  <div class="abs scroll-line"></div>
  <svg class="abs" style="left:595px;top:486px" width="10" height="8"><path d="M1 1 L5 6 L9 1" stroke="#fff" fill="none"/></svg>
</section>

<header class="site-header">
  <div class="brand"><span class="mark"></span>ZELMOR</div>
  <nav class="main-nav">
    <a style="left:413px" href="#">Home</a>
    <a style="left:486px" href="#">About Us</a>
    <a style="left:575px" href="#">Services</a>
    <a style="left:660px" href="#">Team</a>
    <a style="left:729px" href="#">Contact Us</a>
  </nav>
  <div class="header-phone"><svg width="10" height="10" viewBox="0 0 24 24"><path d="M6 2 L10 7 L8 10 Q10 14 14 16 L17 14 L22 18 L19 22 Q8 21 2 5Z" fill="none" stroke="#fff" stroke-width="2"/></svg>123-456-7890</div>
</header>

<section class="about">
  <div class="label" style="top:54px">ABOUT US</div>
  <div class="photo market" role="img" aria-label="Photo of a busy open-air street market under umbrellas"></div>
  <p class="lead">ZELMOR is a premier consulting firm that specialises in aiding global corporations and emerging businesses to enter and scale within Africa's dynamic markets.</p>
  <p class="body">Through swift, actionable insights and innovative strategies, ZELMOR empowers clients to capitalise on Africa's untapped potential, thereby catering specifically to forward-thinking entities poised for exponential growth.</p>
  <div class="abs ghost-square"></div>
  <a class="btn" style="left:406px;top:451px">Explore more&nbsp; →</a>
  <div class="photo street" role="img" aria-label="Photo of a consultant speaking with local market traders"></div>
</section>

<section class="services">
  <div class="label" style="top:79px">OUR SERVICES</div>
  <div class="abs service-icon"><svg width="63" height="64" viewBox="0 0 63 64" fill="none" stroke="#0169c1" stroke-width="1.5"><path d="M18 48 V40 M24 48 V34 M30 48 V38 M36 48 V30 M42 48 V36 M14 49 H48"/><path d="M16 34 L26 26 L32 30 L44 20"/><circle cx="44" cy="18" r="5"/></svg></div>
  <div class="abs service-rule"></div>
  <div class="abs service-marker"></div>
  <ul class="service-list">
    <li>Immersive Research</li>
    <li class="active">Market Sizing</li>
    <li>DeClutter</li>
    <li>Clarity in Chaos</li>
    <li>Engaging Local Consumers</li>
    <li>Research on the Ground</li>
  </ul>
  <p class="body">Lorem Ipsum is simply dummy text of the printing typesetting industry. Lorem Ipsum has been the industry's standard dummy text ever since the 1500s, when an unknown printer took a galley of type and scrambled it to make.</p>
  <a class="btn" style="left:406px;top:560px">Discover more →</a>
  <div class="photo dash" role="img" aria-label="Photo of a hand over a glowing data analytics dashboard"></div>
</section>

<section class="process">
  <div class="label" style="top:74px">ZELMOR PROCESS</div>
  <div class="step" style="left:200px">
    <svg width="50" height="50" viewBox="0 0 50 50" fill="none" stroke="#fff" stroke-width="1.5"><circle cx="23" cy="27" r="21"/><circle cx="23" cy="27" r="14"/><circle cx="23" cy="27" r="7"/><path d="M23 27 L44 6 M38 6 H44 V12"/></svg>
    <h3>Client goal definition understanding</h3>
    <p>There are many variations of passages of lorem Ipsum available, but the majority.</p>
  </div>
  <div class="step" style="left:406px">
    <svg width="50" height="50" viewBox="0 0 50 50" fill="none" stroke="#fff" stroke-width="1.5"><rect x="3" y="6" width="40" height="30"/><path d="M23 2 V6 M14 36 L8 48 M32 36 L38 48 M10 30 V24 M16 30 V20 M22 30 V24"/><circle cx="32" cy="24" r="7"/><path d="M37 29 L45 37"/></svg>
    <h3>In-house research and planning</h3>
    <p>There are many variations of passages of lorem Ipsum available, but the majority.</p>
  </div>
  <div class="step" style="left:612px">
    <svg width="50" height="50" viewBox="0 0 50 50" fill="none" stroke="#fff" stroke-width="1.5"><rect x="3" y="10" width="40" height="28"/><path d="M17 38 V44 M29 38 V44 M12 46 H34 M10 20 L16 26 L24 16"/><rect x="26" y="4" width="16" height="22" fill="#333"/><path d="M29 10 H39 M29 15 H39 M29 20 H39"/></svg>
    <h3>Ground level research and data gathering</h3>
    <p>There are many variations of passages of lorem Ipsum available, but the majority.</p>
  </div>
  <div class="step" style="left:818px">
    <svg width="50" height="50" viewBox="0 0 50 50" fill="none" stroke="#fff" stroke-width="1.5"><path d="M12 4 A10 10 0 1 0 22 14 H12Z"/><path d="M28 6 H46 M28 12 H46 M28 18 H46"/><rect x="3" y="28" width="20" height="18"/><path d="M7 44 V38 M12 44 V34 M17 44 V36"/><rect x="27" y="28" width="20" height="18"/><path d="M29 42 L35 34 L40 38 L45 31"/></svg>
    <h3>Analytical report creations</h3>
    <p>There are many variations of passages of lorem Ipsum available, but the majority.</p>
  </div>
  <svg class="wave" style="left:298px" width="54" height="14"><path d="M2 10 Q14 0 26 7 T52 5" stroke="#ccc" fill="none"/></svg>
  <svg class="wave" style="left:506px" width="54" height="14"><path d="M2 10 Q14 0 26 7 T52 5" stroke="#ccc" fill="none"/></svg>
  <svg class="wave" style="left:709px" width="54" height="14"><path d="M2 10 Q14 0 26 7 T52 5" stroke="#ccc" fill="none"/></svg>
  <a class="btn boxed" style="left:200px;top:364px;width:94px">Contact us&nbsp; →</a>
</section>

<footer class="contact">
  <div class="label" style="top:74px">CONTACT US</div>
  <div class="brand"><span class="mark"></span>ZELMOR</div>
  <h2>Let’s grow together</h2>
  <p class="sub">Have questions about your next growth move? Zelmor has answers.</p>
  <a class="btn" style="left:406px;top:254px">Contact us&nbsp; →</a>
  <ul class="contact-list">
    <li><svg width="13" height="13" viewBox="0 0 24 24"><path d="M6 2 L10 7 L8 10 Q10 14 14 16 L17 14 L22 18 L19 22 Q8 21 2 5Z" fill="none" stroke="#1a78c9" stroke-width="2"/></svg>123-456-7890</li>
    <li><svg width="13" height="13" viewBox="0 0 24 24"><rect x="2" y="5" width="20" height="14" fill="none" stroke="#1a78c9" stroke-width="2"/><path d="M2 6 L12 13 L22 6" fill="none" stroke="#1a78c9" stroke-width="2"/></svg>info@zelmorafricaconsulting.com</li>
    <li><svg width="13" height="13"><rect x="1.5" y="1.5" width="10" height="10" fill="none" stroke="#1a78c9"/></svg><a class="current" href="https://pictova.example/zelmorafrica/">Pictova</a></li>
    <li><svg width="13" height="13"><rect x="1.5" y="1.5" width="10" height="10" fill="none" stroke="#1a78c9"/></svg><a href="https://workfolk.example/company/zelmorafrica/">Workfolk</a></li>
  </ul>
  <div class="abs ghost-square"></div>
  <div class="abs footer-rule"></div>
  <p class="copyright">© 2023 <span>Zelmor Africa</span>. All Rights Reserved &nbsp;&nbsp;&nbsp;|&nbsp;&nbsp;&nbsp; Privacy Policy</p>
</footer>

</body>
</html>
```